BRINEWOOD PRODUCTIONS Video/Photo for Wedding/Events

We need a web design including the code which will be ready to launch. we are a Video and photography company in New Zealand and focus on medium to large Weddings and events.
The site will be our main point of contact with our customers with no more than 4-5 pages (Home, Pricing, Photo/Video Gallery, Contact) and we would like to be able to change the content of all pages as needed. The photos will be uploaded to our website but the videos we can only put the YouTube link.
I will add our company logo and some photos we have already taken to give you an idea of our product and services and can be used in the site as well.

Our pricing section will have photos, videos and photos + videos in 3 different pricing plans which we can upload and change as we need.

Here are some web pages to give you an idea of our industry and our competitors sites, however we would like the quality and design of our work to be better than all of our competitors sites which are listed below.

http://www.tallowpixel.example.nz/2012/02/9-great-new-zealand-photographers-websites/
http://rubquiphotography.example.uk/
http://www.doretavossphotography.example.nz/

Target Market(s)

our target audience is medium to up market customers who are looking at booking their wedding video/photography as well as events

Industry/Entity Type

Industry

Requirements
Must have
• The page must have a minimum of 4 pages, however we would like the designers to look outside the box and be creative with their designs.
Nice to have
• similar colors to our logo but don't limit your self and keep an open mind.

```html
<!DOCTYPE html>
<html lang="en">
<head>
<meta charset="utf-8">
<title>Brinewood Productions — Wedding &amp; Event Video and Photography</title>
<link rel="stylesheet" href="https://fonts.googleapis.com/css2?family=Josefin+Sans:wght@300;400&family=Arimo:wght@400;700&display=swap">
<style>
  :root {
    --sidebar-teal: #8ed2dc;
    --welcome-teal: #6cbccb;
    --ink: #1d2628;
    --logo-grey: #4a4a4c;
    --logo-sub: #9a9a9a;
    --topbar: #3a3836;
    --rule-teal: #5cc3d2;
    --gallery-bg: #2a2620;
    --button-dark: #1f2b2d;
    --button-teal: #4fb9c9;
    --white: #ffffff;
  }
  * { box-sizing: border-box; margin: 0; padding: 0; }
  html, body { width: 1200px; height: 930px; overflow: hidden; background: #222; }
  body { font-family: "Arimo", Arial, sans-serif; }
  .page { position: relative; width: 1200px; height: 930px; overflow: hidden; }

  /* Sidebar */
  .sidebar { position: absolute; left: 0; top: 0; width: 234px; height: 930px; background: var(--sidebar-teal); }
  .brand { position: absolute; left: 0; top: 0; width: 234px; height: 232px; }
  .brand-bg { position: absolute; inset: 0; }
  .brand-mark { position: absolute; left: 93px; top: 48px; width: 48px; height: 48px; border-radius: 50%; background: var(--logo-grey); }
  .brand-name { position: absolute; left: 0; width: 234px; text-align: center; font-family: "Josefin Sans", sans-serif; font-weight: 400; color: var(--logo-grey); }
  .brand-name.primary { top: 146px; font-size: 23px; letter-spacing: 1.5px; }
  .brand-name.secondary { top: 176px; font-size: 11px; letter-spacing: 4px; }

  .main-nav { position: absolute; top: 246px; left: 0; width: 234px; list-style: none; }
  .main-nav li { height: 36px; display: flex; align-items: center; justify-content: center; font-family: "Josefin Sans", sans-serif; font-size: 17px; color: var(--ink); letter-spacing: .5px; position: relative; }
  .main-nav .current svg { position: absolute; left: 77px; top: 2px; }

  .dotted-rule { position: absolute; left: 0; width: 234px; height: 5px; border-top: 2px dotted #2f4a4f; border-bottom: 2px dotted #2f4a4f; }

  .welcome { position: absolute; left: 0; top: 404px; width: 234px; height: 272px; background: var(--welcome-teal); padding: 16px 24px 0; color: var(--ink); }
  .welcome h2 { font-family: "Josefin Sans", sans-serif; font-weight: 400; font-size: 26px; letter-spacing: .5px; margin-bottom: 9px; }
  .welcome p { font-size: 10.3px; line-height: 16.4px; color: #2a3d40; }
  .welcome p strong { color: var(--ink); }
  .read-more { position: absolute; left: 23px; top: 231px; width: 95px; height: 23px; background: var(--button-dark); color: var(--white); font-family: "Josefin Sans", sans-serif; font-size: 12.5px; letter-spacing: .8px; display: flex; align-items: center; justify-content: center; padding-top: 2px; }

  .tweets { position: absolute; left: 25px; top: 697px; width: 190px; color: var(--ink); }
  .tweets h3 { font-family: "Josefin Sans", sans-serif; font-weight: 400; font-size: 19px; letter-spacing: .8px; display: flex; align-items: center; gap: 9px; }
  .tweets h3 .dot { width: 26px; height: 26px; border: 2px solid var(--ink); border-radius: 50%; }
  .tweet-handle { font-size: 10.5px; font-weight: 700; margin-top: 17px; }
  .tweet-body { font-size: 10.3px; line-height: 13.5px; margin-top: 9px; }
  .tweet-time { font-size: 10.3px; font-weight: 700; margin-top: 3px; }

  .copyright { position: absolute; left: 0; top: 880px; width: 224px; text-align: center; font-size: 12px; line-height: 19px; color: var(--ink); }

  /* Top bar */
  .topbar { position: absolute; left: 234px; top: 0; width: 966px; height: 34px; background: var(--topbar); border-bottom: 2px dotted var(--rule-teal); }
  .social { position: absolute; right: 10px; top: 6px; display: flex; gap: 4px; list-style: none; }
  .social li { width: 19px; height: 19px; border-radius: 50%; border: 1.5px solid #e8e8e8; background: #555; }

  /* Hero */
  .hero { position: absolute; left: 234px; top: 34px; width: 966px; height: 609px;
    background:
      radial-gradient(ellipse 60% 30% at 55% 92%, #f4eea0 0%, #e6dd7a 45%, rgba(230,221,122,0) 100%),
      radial-gradient(ellipse 30% 40% at 10% 30%, #c86a7a 0%, rgba(200,106,122,0) 70%),
      radial-gradient(ellipse 60% 40% at 60% 20%, #6f7a2e 0%, rgba(111,122,46,0) 80%),
      linear-gradient(180deg, #4a4a28 0%, #5a4a5e 45%, #4a3a5c 70%, #d9d278 100%); }
  .hero-title { position: absolute; right: 103px; top: 320px; text-align: right; color: var(--white); font-family: "Josefin Sans", sans-serif; font-weight: 300; }
  .hero-title .line-1 { display: block; font-size: 60px; letter-spacing: 1px; line-height: 60px; }
  .hero-title .line-2 { display: block; font-size: 31px; font-weight: 400; letter-spacing: .5px; line-height: 34px; }
  .hero-arrow { position: absolute; top: 281px; }
  .hero-arrow.prev { left: 0; }
  .hero-arrow.next { right: 0; }

  /* Gallery */
  .gallery { position: absolute; left: 234px; top: 643px; width: 966px; height: 287px; background: var(--gallery-bg); }
  .gallery h2 { position: absolute; left: 48px; top: 30px; font-family: "Josefin Sans", sans-serif; font-weight: 400; font-size: 24px; color: var(--white); letter-spacing: 1px; }
  .view-gallery { position: absolute; left: 830px; top: 18px; width: 103px; height: 22px; background: var(--button-teal); color: var(--button-dark); font-family: "Josefin Sans", sans-serif; font-size: 12px; display: flex; align-items: center; justify-content: center; padding-top: 2px; }
  .gallery-rule { position: absolute; left: 48px; top: 62px; width: 885px; border-top: 2px dotted #6a665c; }
  .gallery-thumb { position: absolute; top: 82px; width: 286px; height: 190px; border: 3px solid #5a5852; }
  .thumb-1 { left: 46px; background: linear-gradient(135deg, #cfcfcf 0%, #8b8b8b 40%, #3c3640 100%); }
  .thumb-2 { left: 346px; border-color: #9a9a9a; background: linear-gradient(180deg, #f2f2f2 0%, #d8c3a5 45%, #a9896a 100%); }
  .thumb-3 { left: 647px; border-color: #333; background: linear-gradient(180deg, #1f2a1a 0%, #3a4a2c 40%, #c9c6c0 100%); }
</style>
</head>
<body>
<div class="page">

  <aside class="sidebar">
    <div class="brand">
      <svg class="brand-bg" width="234" height="232" viewBox="0 0 234 232">
        <path d="M0 0H234V214L117 231L0 214Z" fill="#ffffff"/>
        <path d="M0 214L117 231L234 214" fill="none" stroke="#6cbccb" stroke-width="3"/>
      </svg>
      <span class="brand-mark"></span>
      <div class="brand-name primary">BRINEWOOD</div>
      <div class="brand-name secondary">PRODUCTIONS</div>
    </div>

    <ul class="main-nav">
      <li class="current">
        <svg width="80" height="32" viewBox="0 0 80 32"><path d="M8 2H72L79 16L72 30H8L1 16Z" fill="none" stroke="#1d2628" stroke-width="1"/><path d="M10 5H70L76 16L70 27H10L4 16Z" fill="none" stroke="#1d2628" stroke-width="1"/></svg>
        HOME
      </li>
      <li>PRICING</li>
      <li>PHOTO/VIDEO GALLERY</li>
      <li>CONTACT</li>
    </ul>

    <div class="dotted-rule" style="top:399px"></div>

    <section class="welcome">
      <h2>WELCOME!</h2>
      <p><strong>Lorem ipsum dolor sit amet, consectetuer adipiscing elit, sed diam nonummy nibh euismod tincidunt ut laoreet dolore magna aliquam erat volutpat.</strong> Ut wisi enim ad minim veniam, quis nostrud exerci tation ullamcorper suscipit lobortis nisl ut aliquip ex ea commodo consequat. Duis autem vel eum iriure dolor in hendrerit in vulputate velit.</p>
      <a class="read-more">READMORE</a>
    </section>

    <div class="dotted-rule" style="top:675px"></div>

    <section class="tweets">
      <h3>LATEST TWEETS <span class="dot"></span></h3>
      <div class="tweet-handle">@henrik solvang</div>
      <div class="tweet-body">Lorem ipsum dolor sit amet, consectetuer adipiscing elit, sed diam nonummy nibh e</div>
      <div class="tweet-time">3 hours ago</div>
    </section>

    <div class="dotted-rule" style="top:855px"></div>

    <p class="copyright">Copyright ©2013 Brinewood<br>Productions</p>
  </aside>

  <header class="topbar">
    <ul class="social">
      <li></li><li></li><li></li><li></li><li></li>
    </ul>
  </header>

  <section class="hero" role="img" aria-label="Soft-focus wedding ceremony photograph with white flower petals in the foreground and garden lights behind">
    <svg class="hero-arrow prev" width="62" height="135" viewBox="0 0 62 135">
      <path d="M0 0A62 68 0 0 1 0 135Z" fill="rgba(60,45,40,.55)"/>
      <path d="M40 36L10 67L40 98" fill="none" stroke="#ffffff" stroke-width="5"/>
    </svg>
    <h1 class="hero-title"><span class="line-1">BRINEWOOD</span><span class="line-2">PRODUCTIONS</span></h1>
    <svg class="hero-arrow next" width="67" height="135" viewBox="0 0 67 135">
      <path d="M67 0A67 68 0 0 0 67 135Z" fill="rgba(40,30,50,.45)"/>
      <path d="M27 36L57 67L27 98" fill="none" stroke="#ffffff" stroke-width="5"/>
    </svg>
  </section>

  <section class="gallery">
    <h2>GALLERY</h2>
    <a class="view-gallery">VIEW GALLERY</a>
    <div class="gallery-rule"></div>
    <div class="gallery-thumb thumb-1" role="img" aria-label="Wedding photo: ring being placed on the bride's hand"></div>
    <div class="gallery-thumb thumb-2" role="img" aria-label="Wedding photo: bride and groom portrait"></div>
    <div class="gallery-thumb thumb-3" role="img" aria-label="Wedding photo: white ceremony chairs with flower arrangements"></div>
  </section>

</div>
</body>
</html>
```